SUPER EAZY VIDEO BOOK DESIGN, HAVE FUN AND MAKE IT YOUR OWN

SUPER EAZY JUST CHANGE COLORS TO OUR COLORS OF PINK AND AND LOGO, YOU CAN KEEP DESIGN OR MAKE IT YOUR OWN. As you can see I uploaded the vetaCare video mailer, we are keeping all the information the same we are just changing the logo and Web information and email information. everything else is the same. so plenty of time to be creative

Target Market(s)

is Patients with Cancer

Font styles to use
Sans Serif

Colors

Designer to choose colors to be used in the design.

Requirements
Must have
• it must be in our colors I attached our colors, Where it says WEB: put new websites aQuickDabber.com & vetacarealliance.com. Where it says EMAIL: put info@aquickdabber.com
Nice to have
• on the back of the design I would like to add these words : The Test you Take for Them. Will You give Your Love Ones the information to Beat Cancer in Their Lives?
• and place a half Pink and half Blue cancer ribbon in the design on the back
Should not have
• Do not add any words that are not already on the design or in this brief

```html
<!DOCTYPE html>
<html lang="en">
<head>
<meta charset="utf-8">
<title>Video Mailer Dieline – Hereditary Cancer Screening</title>
<link href="https://fonts.googleapis.com/css2?family=Arimo:wght@400;700&family=Arvo:wght@700&family=Space+Mono&family=Tinos&display=swap" rel="stylesheet">
<style>
  :root{
    --navy:#0b1b5a;
    --ink:#2b2f7e;
    --blue-deep:#1a6aa6;
    --blue-mid:#5b9bd5;
    --blue-soft:#6a9cca;
    --pink-soft:#f38fb5;
    --pink:#d6186f;
    --cut:#e0307f;
    --fold:#9a4fa0;
    --screen:#8bc34a;
    --paper:#ffffff;
  }
  html,body{margin:0;padding:0;width:1200px;height:1200px;overflow:hidden;background:var(--paper);}
  .sheet{display:block;width:1200px;height:1200px;}
  .dim-label{font-family:"Arimo",sans-serif;font-size:9px;fill:#222;}
  .slug{font-family:"Space Mono",monospace;font-size:4.5px;fill:#333;}
  .contact{font-family:"Tinos",serif;font-size:11.5px;fill:var(--paper);}
  .disclaimer{font-family:"Tinos",serif;font-size:3.6px;fill:var(--paper);}
  .brand-name{font-family:"Arimo",sans-serif;font-weight:700;font-size:30px;fill:var(--blue-deep);}
  .headline{font-family:"Arvo",serif;font-weight:700;font-size:23px;fill:var(--ink);}
  .tagline{font-family:"Space Mono",monospace;font-size:13px;fill:var(--pink);}
  .cancer-list{font-family:"Tinos",serif;font-size:9.5px;fill:var(--ink);}
  .tab-label{font-family:"Arimo",sans-serif;font-weight:700;font-size:7.5px;fill:var(--navy);}
  .tab-text{font-family:"Arimo",sans-serif;font-size:11px;fill:var(--paper);}
  .btn-num{font-family:"Tinos",serif;font-size:11px;fill:var(--paper);}
</style>
</head>
<body>
<svg class="sheet" viewBox="0 0 1920 1920" xmlns="http://www.w3.org/2000/svg">
  <defs>
    <linearGradient id="photoTone" x1="0" y1="0" x2="1" y2="1">
      <stop offset="0" stop-color="#c9b8a3"/>
      <stop offset="0.5" stop-color="#a57a5e"/>
      <stop offset="1" stop-color="#d9a58a"/>
    </linearGradient>
  </defs>

  <!-- print marks -->
  <g class="print-marks" fill="none" stroke="#222" stroke-width="0.8">
    <circle cx="168" cy="724" r="6" fill="#888" stroke="none"/>
    <g><circle cx="195" cy="724" r="3.5"/><line x1="188" y1="724" x2="202" y2="724"/><line x1="195" y1="717" x2="195" y2="731"/></g>
    <g><circle cx="168" cy="751" r="3.5"/><line x1="161" y1="751" x2="175" y2="751"/><line x1="168" y1="744" x2="168" y2="758"/></g>
    <g><circle cx="1776" cy="724" r="3.5"/><line x1="1769" y1="724" x2="1783" y2="724"/><line x1="1776" y1="717" x2="1776" y2="731"/></g>
    <g><circle cx="1803" cy="751" r="3.5"/><line x1="1796" y1="751" x2="1810" y2="751"/><line x1="1803" y1="744" x2="1803" y2="758"/></g>
    <g><circle cx="168" cy="1185" r="3.5"/><line x1="161" y1="1185" x2="175" y2="1185"/><line x1="168" y1="1178" x2="168" y2="1192"/></g>
    <g><circle cx="195" cy="1212" r="3.5"/><line x1="188" y1="1212" x2="202" y2="1212"/><line x1="195" y1="1205" x2="195" y2="1219"/></g>
    <g><circle cx="1803" cy="1185" r="3.5"/><line x1="1796" y1="1185" x2="1810" y2="1185"/><line x1="1803" y1="1178" x2="1803" y2="1192"/></g>
    <g><circle cx="1776" cy="1212" r="3.5"/><line x1="1769" y1="1212" x2="1783" y2="1212"/><line x1="1776" y1="1205" x2="1776" y2="1219"/></g>
    <circle cx="1803" cy="1212" r="6" fill="#888" stroke="none"/>
  </g>
  <text class="slug" x="209" y="722">vetaCare_VideoMailer_Template2.pdf   1   2018-09-30   19:15</text>

  <g class="color-bar">
    <rect x="163" y="926" width="10" height="10" fill="#00a0e3"/>
    <rect x="163" y="936" width="10" height="10" fill="#e4007f"/>
    <rect x="163" y="947" width="10" height="10" fill="#ffec00"/>
    <rect x="163" y="957" width="10" height="10" fill="#1d2088"/>
    <rect x="163" y="968" width="10" height="10" fill="#e60012"/>
    <rect x="163" y="978" width="10" height="10" fill="#009944"/>
    <rect x="163" y="989" width="10" height="21" fill="#231815"/>
    <rect x="1798" y="926" width="10" height="10" fill="#00a0e3"/>
    <rect x="1798" y="936" width="10" height="10" fill="#e4007f"/>
    <rect x="1798" y="947" width="10" height="10" fill="#ffec00"/>
    <rect x="1798" y="957" width="10" height="10" fill="#1d2088"/>
    <rect x="1798" y="968" width="10" height="10" fill="#e60012"/>
    <rect x="1798" y="978" width="10" height="10" fill="#009944"/>
    <rect x="1798" y="989" width="10" height="21" fill="#231815"/>
  </g>
  <g class="gray-scale">
    <rect x="932" y="1207" width="11" height="10" fill="#000"/>
    <rect x="943" y="1207" width="11" height="10" fill="#1a1a1a"/>
    <rect x="954" y="1207" width="11" height="10" fill="#333"/>
    <rect x="965" y="1207" width="11" height="10" fill="#4d4d4d"/>
    <rect x="976" y="1207" width="11" height="10" fill="#666"/>
    <rect x="987" y="1207" width="11" height="10" fill="#808080"/>
    <rect x="998" y="1207" width="11" height="10" fill="#999"/>
    <rect x="1009" y="1207" width="11" height="10" fill="#b3b3b3"/>
    <rect x="1020" y="1207" width="11" height="10" fill="#ccc"/>
    <rect x="1031" y="1207" width="8" height="10" fill="#e6e6e6"/>
  </g>

  <!-- dimension lines -->
  <g class="dimensions" stroke="var(--cut)" stroke-width="0.8" fill="none">
    <line x1="247" y1="791" x2="1727" y2="791"/>
    <line x1="247" y1="776" x2="247" y2="806"/>
    <line x1="261" y1="776" x2="261" y2="806"/>
    <line x1="620" y1="776" x2="620" y2="806"/>
    <line x1="634" y1="776" x2="634" y2="806"/>
    <line x1="994" y1="776" x2="994" y2="806"/>
    <line x1="1010" y1="776" x2="1010" y2="806"/>
    <line x1="1371" y1="776" x2="1371" y2="806"/>
    <line x1="1727" y1="776" x2="1727" y2="806"/>
    <line x1="1745" y1="850" x2="1745" y2="1103"/>
    <line x1="1732" y1="850" x2="1760" y2="850"/>
    <line x1="1732" y1="1103" x2="1760" y2="1103"/>
  </g>
  <g class="dim-labels">
    <rect x="428" y="784" width="22" height="14" fill="#fff"/>
    <rect x="784" y="784" width="32" height="14" fill="#fff"/>
    <rect x="1183" y="784" width="16" height="14" fill="#fff"/>
    <rect x="1525" y="784" width="34" height="14" fill="#fff"/>
    <rect x="1738" y="950" width="20" height="30" fill="#fff"/>
    <text class="dim-label" x="246" y="769">8mm</text>
    <text class="dim-label" x="427" y="783">209mm</text>
    <text class="dim-label" x="617" y="767">8mm</text>
    <text class="dim-label" x="790" y="790">210mm</text>
    <text class="dim-label" x="993" y="771">9.5mm</text>
    <text class="dim-label" x="1177" y="782">210.5mm</text>
    <text class="dim-label" x="1525" y="780">207.5mm</text>
    <text class="dim-label" x="1738" y="965">148mm</text>
  </g>

  <!-- panel 1 : video screen cover with flaps -->
  <g class="cover-panel">
    <path d="M283 815 H598 L620 836 V1116 L598 1137 H283 L261 1116 V1103 L248 1103 L228 1083 V870 L248 850 H261 V836 Z" fill="var(--navy)"/>
    <path d="M400 888 C470 884 510 905 560 909 C590 910 610 902 620 895 V1103 H350 C300 1080 268 1040 268 990 C268 930 320 892 400 888 Z" fill="var(--paper)"/>
    <rect class="screen-window" x="344" y="899" width="190" height="106" fill="none" stroke="var(--screen)" stroke-width="0.8"/>
    <g class="controls">
      <circle cx="325" cy="1035" r="8" fill="var(--navy)" stroke="var(--screen)" stroke-width="0.8"/>
      <text class="btn-num" x="325" y="1039" text-anchor="middle">1</text>
      <circle cx="358" cy="1035" r="8" fill="var(--blue-deep)" stroke="var(--screen)" stroke-width="0.8"/>
      <text class="btn-num" x="358" y="1039" text-anchor="middle">2</text>
      <circle cx="391" cy="1035" r="8" fill="var(--blue-mid)" stroke="var(--screen)" stroke-width="0.8"/>
      <text class="btn-num" x="391" y="1039" text-anchor="middle">3</text>
      <circle cx="424" cy="1035" r="8" fill="var(--pink-soft)" stroke="var(--screen)" stroke-width="0.8"/>
      <text class="btn-num" x="424" y="1039" text-anchor="middle">4</text>
      <circle cx="457" cy="1035" r="8" fill="var(--pink)" stroke="var(--screen)" stroke-width="0.8"/>
      <text class="btn-num" x="457" y="1039" text-anchor="middle">5</text>
      <circle cx="490" cy="1035" r="8" fill="#fff" stroke="var(--screen)" stroke-width="0.8"/>
      <path d="M485 1031 L489 1035 L485 1039 Z M491 1031 V1039 M494 1031 V1039" stroke="#111" stroke-width="1" fill="#111"/>
      <circle cx="523" cy="1035" r="8" fill="#fff" stroke="var(--screen)" stroke-width="0.8"/>
      <path d="M518 1033 H520 L523 1030 V1040 L520 1037 H518 Z" fill="#111"/>
      <line x1="524" y1="1035" x2="529" y2="1035" stroke="#111" stroke-width="1.2"/>
      <circle cx="556" cy="1035" r="8" fill="#fff" stroke="var(--screen)" stroke-width="0.8"/>
      <path d="M550 1033 H552 L555 1030 V1040 L552 1037 H550 Z" fill="#111"/>
      <path d="M556 1035 H562 M559 1032 V1038" stroke="#111" stroke-width="1.2"/>
    </g>
    <rect x="524" y="1104" width="12" height="6" fill="#fff" stroke="var(--cut)" stroke-width="0.6"/>
    <g fill="none" stroke="var(--cut)" stroke-width="0.8">
      <path d="M283 815 H598 L620 836 V1116 L598 1137 H283 L261 1116 V1103 L248 1103 L228 1083 V870 L248 850 H261 V836 Z"/>
    </g>
    <g fill="none" stroke="var(--fold)" stroke-width="0.6">
      <line x1="261" y1="836" x2="620" y2="836"/>
      <line x1="261" y1="850" x2="620" y2="850"/>
      <line x1="261" y1="1103" x2="620" y2="1103"/>
      <line x1="261" y1="850" x2="261" y2="1103"/>
      <line x1="248" y1="850" x2="248" y2="1103"/>
    </g>
  </g>

  <!-- panel 2 : family photo and contact -->
  <g class="photo-panel">
    <rect x="634" y="850" width="360" height="253" fill="var(--paper)"/>
    <path d="M634 990 C720 1045 850 1052 994 1044 V1103 H634 Z" fill="var(--blue-mid)"/>
    <path d="M740 850 H994 V980 C970 960 950 955 935 960 C960 930 975 900 980 870 C900 880 830 885 790 875 C765 868 750 860 740 850 Z" fill="var(--pink)"/>
    <path d="M634 850 H760 C800 880 880 885 960 862 C940 930 900 990 840 1015 C780 1035 690 1030 634 990 Z" fill="url(#photoTone)" role="img" aria-label="Photograph of a smiling multi-generation family: grandparents, parents, a young girl and a baby"/>
    <path d="M805 1028 C830 1020 860 1005 875 992 C882 1012 882 1030 872 1038 C852 1040 830 1038 818 1046 Z" fill="var(--pink-soft)"/>
    <text class="contact" x="637" y="1060">PHONE: 877-555-0148</text>
    <text class="contact" x="637" y="1071">WEB: aQuickDabber.com &amp; vetacarealliance.com</text>
    <text class="contact" x="637" y="1082">EMAIL: info@aquickdabber.com</text>
    <text class="disclaimer" x="637" y="1091" textLength="352">The information contained herein is not intended to replace a one-to-one relationship with a doctor or qualified healthcare professional. It is shared as general</text>
    <text class="disclaimer" x="637" y="1096" textLength="335">knowledge only. We encourage you to make your own health care decisions based on research and in partnership with a qualified healthcare</text>
    <text class="disclaimer" x="637" y="1101" textLength="320">professional. These statements have not been evaluated by any agency and are not intended to diagnose, treat, cure or prevent any disease.</text>
  </g>

  <!-- panel 3 : front cover -->
  <g class="front-panel">
    <rect x="1010" y="850" width="361" height="253" fill="var(--paper)"/>
    <path d="M1010 1072 C1110 1060 1200 1075 1260 1090 C1310 1100 1350 1080 1371 1050 V1103 H1010 Z" fill="var(--blue-soft)"/>
    <path d="M1320 850 H1371 V965 C1355 950 1345 945 1330 945 C1310 945 1290 955 1278 958 C1310 935 1312 905 1305 880 C1300 865 1308 855 1320 850 Z" fill="var(--pink)"/>
    <g class="brand-lockup">
      <circle cx="1060" cy="922" r="8" fill="var(--pink)"/>
      <text class="brand-name" x="1074" y="933">A Quick Dabber</text>
    </g>
    <text class="headline" x="1054" y="990" textLength="312" lengthAdjust="spacingAndGlyphs">Hereditary Cancer Screening</text>
    <text class="tagline" x="1052" y="1009" textLength="278" lengthAdjust="spacingAndGlyphs">“The test you order FOR your patients”</text>
    <text class="cancer-list" x="1190" y="1047" text-anchor="middle">PROSTATE | COLORECTAL | MELANOMA | ENDOMETRIAL</text>
    <text class="cancer-list" x="1190" y="1057" text-anchor="middle">GASTRIC | PANCREATIC | BREAST | OVARIAN</text>
  </g>

  <!-- panel 4 : question tabs -->
  <g class="question-panel">
    <g class="tab">
      <path d="M1371 850 H1727 V890 Q1727 898 1719 898 H1371 Z" fill="var(--navy)"/>
      <circle cx="1398" cy="874" r="26" fill="#fff"/>
      <text class="tab-label" x="1398" y="871" text-anchor="middle">How can</text>
      <text class="tab-label" x="1398" y="880" text-anchor="middle">I help?</text>
      <text class="tab-text" x="1434" y="870">You can know if your patients have a</text>
      <text class="tab-text" x="1434" y="883">higher risk of getting cancer!</text>
      <circle cx="1700" cy="874" r="16" fill="none" stroke="#fff" stroke-width="2"/>
      <path d="M1700 884 L1691 875 C1686 869 1692 862 1697 865 L1700 868 L1703 865 C1708 862 1714 869 1709 875 Z" fill="#fff"/>
    </g>
    <g class="tab">
      <path d="M1371 901 H1719 Q1727 901 1727 909 V941 Q1727 949 1719 949 H1371 Z" fill="var(--blue-deep)"/>
      <circle cx="1398" cy="925" r="26" fill="#fff"/>
      <text class="tab-label" x="1398" y="922" text-anchor="middle">Who do</text>
      <text class="tab-label" x="1398" y="931" text-anchor="middle">we test?</text>
      <text class="tab-text" x="1434" y="929">What is the medical necessity for this test?</text>
      <circle cx="1700" cy="925" r="16" fill="none" stroke="#fff" stroke-width="2"/>
      <circle cx="1700" cy="920" r="5" fill="none" stroke="#fff" stroke-width="2"/>
      <path d="M1690 937 C1692 928 1708 928 1710 937" fill="none" stroke="#fff" stroke-width="2"/>
    </g>
    <g class="tab">
      <path d="M1371 952 H1719 Q1727 952 1727 960 V992 Q1727 1000 1719 1000 H1371 Z" fill="var(--blue-mid)"/>
      <circle cx="1398" cy="976" r="26" fill="#fff"/>
      <text class="tab-label" x="1398" y="973" text-anchor="middle">How do</text>
      <text class="tab-label" x="1398" y="982" text-anchor="middle">I test?</text>
      <text class="tab-text" x="1434" y="980">Simple swab, 1 minute to test!</text>
      <circle cx="1700" cy="976" r="16" fill="none" stroke="#fff" stroke-width="2"/>
      <path d="M1686 978 H1693 L1696 970 L1700 985 L1703 974 L1705 978 H1714" fill="none" stroke="#fff" stroke-width="1.6"/>
    </g>
    <g class="tab">
      <path d="M1371 1004 H1719 Q1727 1004 1727 1012 V1044 Q1727 1052 1719 1052 H1371 Z" fill="var(--pink-soft)"/>
      <circle cx="1398" cy="1028" r="26" fill="#fff"/>
      <text class="tab-label" x="1398" y="1025" text-anchor="middle">How to start</text>
      <text class="tab-label" x="1398" y="1034" text-anchor="middle">testing</text>
      <text class="tab-text" x="1434" y="1032">Testing in your office is easy!</text>
      <circle cx="1700" cy="1028" r="16" fill="none" stroke="#fff" stroke-width="2"/>
      <path d="M1692 1028 L1698 1035 L1709 1020" fill="none" stroke="#fff" stroke-width="2.4"/>
    </g>
    <g class="tab">
      <path d="M1371 1055 H1719 Q1727 1055 1727 1063 V1103 H1371 Z" fill="var(--pink)"/>
      <circle cx="1398" cy="1079" r="26" fill="#fff"/>
      <text class="tab-label" x="1398" y="1077" text-anchor="middle">Knowledge</text>
      <text class="tab-label" x="1398" y="1086" text-anchor="middle">is Power</text>
      <text class="tab-text" x="1434" y="1069">I don’t want to test.</text>
      <text class="tab-text" x="1441" y="1082">I don’t want to know.</text>
      <text class="tab-text" x="1448" y="1096">I just want to enjoy my life.</text>
      <circle cx="1700" cy="1079" r="16" fill="none" stroke="#fff" stroke-width="2"/>
      <path d="M1695 1074 C1695 1067 1706 1067 1706 1074 C1706 1079 1700 1079 1700 1084" fill="none" stroke="#fff" stroke-width="2"/>
      <circle cx="1700" cy="1089" r="1.5" fill="#fff"/>
    </g>
  </g>

  <!-- cut and fold lines over the strip -->
  <g fill="none" stroke="var(--cut)" stroke-width="0.8">
    <rect x="634" y="850" width="1093" height="253"/>
    <line x1="994" y1="850" x2="994" y2="1103"/>
    <line x1="1010" y1="850" x2="1010" y2="1103"/>
    <line x1="1371" y1="850" x2="1371" y2="1103"/>
  </g>
</svg>
</body>
</html>
```